kovu Apparel - T-Shirts on Shopify

Hi - I'm creating a new site to sell undershirts. The premise of the undershirt is that it has a U-neck shape so that your white undershirt does not show when you are wearing a button shirt. I want the site to be fun but still look stunning because I want to attract a certain clientele (business professionals with a sense of humor). I'm creating a funny video to post on the site to hopefully get some social media buzz.
I want the design to highlight the product but more importantly the lifestyle of the person who wears it. This is an undershirt so nobody really sees it and that's the point.
Since this is a single product that I want to sell, I want to make sure that the design works with Shopify. Since this is not for theme development, this design must work with an existing theme on Shopify (preferably free but if you must then no more than $75). You can choose the theme to design for.
Products:
* Single kovu undershirt in 4 sizes - S, M, L and XL
* 3 packs or 7 packs (buy 6 get 1 free)
* One-time purchase or subscription (delivery every 3 or 6 months) - I know this will require custom theme development
Attached you will find a very rough idea for the site and this was made before I had considered putting in a video (Wix template). It's going to be tough to catch lightning in a bottle much like Penny Razor Guild but that's what I'm hoping for.
Name of the company is kovu Apparel. Logo attached. Included .ai file which has some funky colors so please use the light blue color logo similar to the png's attached.
Here is the site for a competitor. There's much to be improved on the site but I include it here because the concept of the undershirt is the same: http://www.gatheredloomwear.example
Feel free to use stock images that I can purchase on the site that represents a young and cool vibe. I will be taking shots of the shirts for the product page so for now use some generic shirt please.
Reason: Please take a look at feedback for other designs. I'm hoping for my mockup to be an inspiration, not just re-skinning the mockup I created. Plus it must be based on a Shopify theme. Use stock images as necessary but keep the budget for purchasing images under $100.
Target Market(s)
Male 30-50

```html
<!DOCTYPE html>
<html lang="en">
<head>
<meta charset="utf-8">
<title>kovu Apparel</title>
<link href="https://fonts.googleapis.com/css2?family=Oswald:wght@400;500;600;700&family=Open+Sans:wght@400;600;700&family=Montserrat:wght@500&display=swap" rel="stylesheet">
<style>
:root{
  --black:#0d0d0d;
  --white:#ffffff;
  --blue:#2a9ad6;
  --blue-light:#4fb3e6;
  --red:#e4432d;
  --text:#6f6f6f;
  --heading:#2b2b2b;
  --dark:#2f2b2a;
  --dark-panel:#3b3534;
  --footer:#272322;
  --grey-box:#ececec;
  --muted:#9c9696;
}
*{box-sizing:border-box;margin:0;padding:0}
html,body{width:1200px;height:3251px;overflow:hidden}
body{font-family:"Open Sans",Arial,sans-serif;color:var(--text);background:var(--white);position:relative}
.section{position:absolute;left:0;width:1200px}
.abs{position:absolute}
.heading-font{font-family:"Oswald","Arial Narrow",sans-serif;text-transform:uppercase}

/* top bar */
.top-bar{top:0;height:54px;background:var(--black);color:#ddd;font-size:13px}
.top-bar .welcome{left:95px;top:17px}
.top-bar .utility{right:78px;top:17px;display:flex;gap:34px}
.top-bar .utility span{display:flex;align-items:center;gap:8px}

/* header */
.site-header{top:54px;height:114px;background:var(--white)}
.brand{left:119px;top:32px;font-family:"Montserrat",sans-serif;font-weight:500;font-size:42px;color:var(--heading);display:flex;align-items:center;gap:12px}
.brand .mark{width:22px;height:22px;border-radius:50%;background:var(--blue)}
.main-nav{right:84px;top:46px;display:flex;gap:34px;font-family:"Oswald",sans-serif;font-weight:600;font-size:15px;color:var(--heading);align-items:center}

/* hero */
.hero{top:168px;height:442px}
.hero-photo{position:absolute;inset:0;background:linear-gradient(90deg,#c9b7a6 0%,#a9b6c2 28%,#8797a7 55%,#6b7d8e 100%)}
.hero-tag{background:var(--black);color:var(--white);font-family:"Oswald",sans-serif;font-weight:700;text-transform:uppercase;text-align:center}
.hero-tag.small{left:699px;top:125px;width:385px;height:46px;font-size:30px;line-height:46px;letter-spacing:1px}
.hero-tag.big{left:683px;top:184px;width:401px;height:79px;font-size:62px;line-height:79px}
.hero-tag.under{left:767px;top:271px;width:222px;height:38px;font-size:27px;line-height:38px;letter-spacing:6px;clip-path:polygon(0 0,100% 0,88% 100%,12% 100%)}

/* section titles */
.section-title{border:2px solid currentColor;font-family:"Oswald",sans-serif;font-weight:600;font-size:22px;text-transform:uppercase;letter-spacing:1px;text-align:center;line-height:53px}

/* products */
.products{top:610px;height:934px}
.products .section-title{left:452px;top:73px;width:296px;height:57px;color:var(--heading)}
.intro{left:168px;top:170px;width:875px;text-align:center;font-size:12.5px;line-height:25px}
.read-more{font-family:"Oswald",sans-serif;font-weight:600;font-size:13px;text-transform:uppercase;color:var(--heading)}
.products .intro-more{left:0;width:1200px;text-align:center;top:238px}
.product-card{top:297px;width:320px;text-align:center}
.product-image{width:260px;height:258px;margin:0 auto;background:radial-gradient(circle at 50% 45%,#fbfbfb 0%,#ececee 55%,#f6f6f6 100%)}
.product-name{margin-top:47px;font-family:"Oswald",sans-serif;font-weight:600;font-size:15px;color:var(--heading)}
.product-price{margin-top:22px;font-family:"Oswald",sans-serif;font-weight:600;font-size:19px;color:var(--red)}
.product-desc{margin-top:10px;font-size:12px;line-height:18px}
.product-desc b{color:var(--heading)}
.shop-button{left:480px;top:777px;width:238px;height:54px;background:var(--blue);color:var(--white);font-family:"Oswald",sans-serif;font-weight:600;font-size:24px;text-align:center;line-height:54px;clip-path:polygon(0 0,100% 0,92% 100%,8% 100%)}

/* blog */
.blog{top:1544px;height:760px;background:var(--dark)}
.blog .section-title{left:428px;top:84px;width:342px;height:57px;color:var(--white)}
.post{width:300px}
.post-head{display:flex;align-items:center;gap:22px}
.post-num{width:40px;height:44px;background:var(--blue);color:var(--white);font-family:"Oswald",sans-serif;font-weight:600;font-size:26px;text-align:center;line-height:44px}
.post-title{font-family:"Oswald",sans-serif;font-weight:600;font-size:16px;color:var(--white)}
.post-rule{width:52px;height:2px;background:#8a8a8a;margin:8px 0 0 62px}
.post-text{margin-top:10px;font-size:12px;line-height:18px;color:#bdb7b6}
.post .read-more{display:block;margin-top:12px;color:var(--white)}

/* promo */
.promo{left:98px;top:637px;width:1005px;height:122px;background:var(--white);overflow:hidden}
.promo-photo{left:0;top:0;width:150px;height:122px;background:linear-gradient(90deg,#c8d7e2,#b9a797)}
.promo-deal{left:160px;top:42px;font-family:"Oswald",sans-serif;font-weight:600;font-size:19px;line-height:22px;color:var(--heading)}
.promo-cart{left:307px;top:44px}
.promo-offer{left:409px;top:0;width:596px;height:122px;background:var(--blue);clip-path:polygon(4% 0,100% 0,100% 100%,0 100%)}
.promo-offer .line1{left:30px;top:38px;font-family:"Oswald",sans-serif;font-weight:600;font-size:21px;color:var(--white)}
.promo-offer .line2{left:30px;top:67px;font-family:"Oswald",sans-serif;font-weight:500;font-size:15px;color:var(--white)}
.promo-offer .btn{left:446px;top:46px;width:105px;height:48px;border:2px solid var(--white);color:var(--white);font-family:"Oswald",sans-serif;font-weight:600;font-size:14px;text-align:center;line-height:44px}

/* testimonials */
.testimonials{top:2304px;height:494px}
.testimonials .section-title{left:471px;top:96px;width:258px;height:57px;color:var(--heading)}
.testimonial-video{left:98px;top:215px;width:284px;height:217px;background:linear-gradient(135deg,#8a8078,#c9c1b8 60%,#a59d95)}
.play{left:117px;top:84px;width:50px;height:50px;border-radius:50%;background:rgba(40,40,40,.75)}
.testimonial-box{left:390px;top:215px;width:601px;height:217px;background:var(--grey-box);padding:30px 22px}
.testimonial-name{font-family:"Oswald",sans-serif;font-weight:600;font-size:17px;color:var(--heading)}
.testimonial-rule{width:46px;height:2px;background:#999;margin:10px 0 16px}
.testimonial-text{font-size:12px;line-height:19px}
.arrow-btn{top:215px;width:44px;height:44px;background:var(--blue);display:flex;align-items:center;justify-content:center}

/* features */
.features{top:2798px;height:363px;background:var(--dark)}
.feature{top:0;width:336px;height:317px;background:var(--dark-panel)}
.feature-head{height:92px;background:var(--blue);display:flex;align-items:center;justify-content:center;gap:18px;font-family:"Oswald",sans-serif;font-weight:600;font-size:18px;color:var(--white);text-transform:uppercase}
.feature.mid .feature-head{background:var(--blue-light)}
.feature-rule{width:42px;height:2px;background:#cfcfcf;margin:36px auto 0}
.feature-text{margin:18px auto 0;width:240px;text-align:center;font-size:12px;line-height:18px;color:#d6d0cf}
.cards{display:flex;justify-content:center;gap:10px;margin-top:16px}
.cards span{width:48px;height:28px;background:#f2f2f2;border-radius:2px}
.feature-btn{position:absolute;left:100px;bottom:30px;width:136px;height:38px;border:2px solid #d6d0cf;color:var(--white);font-family:"Oswald",sans-serif;font-weight:500;font-size:13px;text-align:center;line-height:34px}

/* footer */
.site-footer{top:3161px;height:90px;background:var(--footer);color:#bdb7b6;font-size:11px}
.site-footer .copyright{left:98px;top:39px}
.site-footer .copyright b{color:var(--white)}
.footer-links{left:414px;top:39px;display:flex;gap:20px;text-transform:uppercase}
.social{left:921px;top:33px;display:flex;gap:14px}
.social span{width:24px;height:24px;border-radius:50%;background:#e8e4e3}
</style>
</head>
<body>

<header class="section top-bar">
  <div class="abs welcome">Welcome to our online store! Login or Signup</div>
  <div class="abs utility">
    <span><svg width="12" height="12" viewBox="0 0 12 12"><circle cx="6" cy="6" r="4" fill="none" stroke="#ddd" stroke-width="2"/></svg>Setting</span>
    <span><svg width="12" height="12" viewBox="0 0 12 12"><circle cx="6" cy="4" r="3" fill="#ddd"/><path d="M1 12a5 5 0 0 1 10 0z" fill="#ddd"/></svg>My Account</span>
    <span><svg width="14" height="12" viewBox="0 0 14 12"><path d="M0 1h3l2 7h7l2-5H4" fill="none" stroke="#ddd" stroke-width="1.5"/><circle cx="6" cy="11" r="1" fill="#ddd"/><circle cx="11" cy="11" r="1" fill="#ddd"/></svg>Cart: 0 item</span>
  </div>
</header>

<div class="section site-header">
  <div class="abs brand"><span>kovu Apparel</span></div>
  <nav class="abs main-nav">
    <span>HOME</span><span>CATEGORIES</span><span>ABOUT US</span><span>FAQs</span><span>CONTACT US</span>
    <svg width="16" height="16" viewBox="0 0 16 16"><circle cx="6.5" cy="6.5" r="5" fill="none" stroke="#2b2b2b" stroke-width="2"/><path d="M10 10l5 5" stroke="#2b2b2b" stroke-width="2"/></svg>
  </nav>
</div>

<section class="section hero">
  <div class="hero-photo" role="img" aria-label="Lifestyle photo of a smiling couple in light shirts against a blue-grey wall"></div>
  <div class="abs hero-tag small">Lorem ipsum dolor</div>
  <div class="abs hero-tag big">Accusantium</div>
  <div class="abs hero-tag under">Unde</div>
</section>

<section class="section products">
  <h2 class="abs section-title">Our new products</h2>
  <p class="abs intro">Lorem ipsum dolor sit amet nem eos illo omnis aut aperiam ab ipsam ipsa odit aut aperiam aut aspernatur veritatis unde sed enim accusantium laudantium sunt perspiciatis ipsam sed doloremque ipsam dolores totam unde aut illo aut veritatis explicabo dicta quia veritatis dicta sunt quasi neque rem</p>
  <span class="abs read-more intro-more">Read more</span>

  <article class="abs product-card" style="left:111px">
    <div class="product-image" role="img" aria-label="Stack of plain white U-neck undershirts"></div>
    <h3 class="product-name">KOVU UNDERSHIRT 01</h3>
    <div class="product-price">$30.00 &nbsp;-&nbsp; $11.00</div>
    <p class="product-desc">ipsum dolor sit amet voluptatem fugit aut<br><b>every six months</b> or <b>only single item</b></p>
  </article>
  <article class="abs product-card" style="left:428px">
    <div class="product-image" role="img" aria-label="Folded white undershirts in a pack"></div>
    <h3 class="product-name">KOVU UNDERSHIRT 01</h3>
    <div class="product-price">$30.00 &nbsp;-&nbsp; $11.00</div>
    <p class="product-desc">ipsum dolor sit amet voluptatem fugit aut<br><b>every six months</b> or <b>only single item</b></p>
  </article>
  <article class="abs product-card" style="left:753px">
    <div class="product-image" role="img" aria-label="Two white V-neck undershirts"></div>
    <h3 class="product-name">KOVU UNDERSHIRT 01</h3>
    <div class="product-price">$30.00 &nbsp;-&nbsp; $11.00</div>
    <p class="product-desc">ipsum dolor sit amet voluptatem fugit aut<br><b>every six months</b> or <b>only single item</b></p>
  </article>

  <div class="abs shop-button">SHOP NOW</div>
</section>

<section class="section blog">
  <h2 class="abs section-title">Lates news from blog</h2>

  <article class="abs post" style="left:98px;top:203px"><div class="post-head"><span class="post-num">1</span><h3 class="post-title">AMET VOLUPTATEM</h3></div><div class="post-rule"></div><p class="post-text">Lorem ipsum dolor sit amet nem illa omnis aperiam ab ipsam ipsa odit aut aperiam aspernatur veritatis unde enim accusantium laudantium laudantium sunt</p><span class="read-more">Read more</span></article>
  <article class="abs post" style="left:452px;top:203px"><div class="post-head"><span class="post-num">2</span><h3 class="post-title">AMET VOLUPTATEM</h3></div><div class="post-rule"></div><p class="post-text">Lorem ipsum dolor sit amet nem illa omnis aperiam ab ipsam ipsa odit aut aperiam aspernatur veritatis unde enim accusantium laudantium laudantium sunt</p><span class="read-more">Read more</span></article>
  <article class="abs post" style="left:807px;top:203px"><div class="post-head"><span class="post-num">3</span><h3 class="post-title">AMET VOLUPTATEM</h3></div><div class="post-rule"></div><p class="post-text">Lorem ipsum dolor sit amet nem illa omnis aperiam ab ipsam ipsa odit aut aperiam aspernatur veritatis unde enim accusantium laudantium laudantium sunt</p><span class="read-more">Read more</span></article>
  <article class="abs post" style="left:98px;top:412px"><div class="post-head"><span class="post-num">4</span><h3 class="post-title">AMET VOLUPTATEM</h3></div><div class="post-rule"></div><p class="post-text">Lorem ipsum dolor sit amet nem illa omnis aperiam ab ipsam ipsa odit aut aperiam aspernatur veritatis unde enim accusantium laudantium laudantium sunt</p><span class="read-more">Read more</span></article>
  <article class="abs post" style="left:452px;top:412px"><div class="post-head"><span class="post-num">5</span><h3 class="post-title">AMET VOLUPTATEM</h3></div><div class="post-rule"></div><p class="post-text">Lorem ipsum dolor sit amet nem illa omnis aperiam ab ipsam ipsa odit aut aperiam aspernatur veritatis unde enim accusantium laudantium laudantium sunt</p><span class="read-more">Read more</span></article>
  <article class="abs post" style="left:807px;top:412px"><div class="post-head"><span class="post-num">6</span><h3 class="post-title">AMET VOLUPTATEM</h3></div><div class="post-rule"></div><p class="post-text">Lorem ipsum dolor sit amet nem illa omnis aperiam ab ipsam ipsa odit aut aperiam aspernatur veritatis unde enim accusantium laudantium laudantium sunt</p><span class="read-more">Read more</span></article>

  <aside class="abs promo">
    <div class="abs promo-photo" role="img" aria-label="Photo of a relaxed couple in casual shirts"></div>
    <div class="abs promo-deal">BUY 6 GET 1<br>FREE</div>
    <svg class="abs promo-cart" width="48" height="40" viewBox="0 0 48 40"><path d="M2 4h8l6 22h24l6-16H13" fill="none" stroke="#2a9ad6" stroke-width="4" stroke-linejoin="round"/><circle cx="19" cy="34" r="4" fill="#2a9ad6"/><circle cx="37" cy="34" r="4" fill="#2a9ad6"/></svg>
    <div class="abs promo-offer">
      <div class="abs line1">ONE - TIME PURCHASE OR SUBSCRIPTION</div>
      <div class="abs line2">DELIVERY EVERY 3 OR 6 MONTHS</div>
      <div class="abs btn">SHOP NOW</div>
    </div>
  </aside>
</section>

<section class="section testimonials">
  <h2 class="abs section-title">What they says</h2>
  <div class="abs testimonial-video" role="img" aria-label="Video still of a man in a white undershirt">
    <div class="abs play"><svg width="50" height="50" viewBox="0 0 50 50"><path d="M20 15l16 10-16 10z" fill="#fff"/></svg></div>
  </div>
  <blockquote class="abs testimonial-box">
    <div class="testimonial-name">JOHN DOE, 25 YO</div>
    <div class="testimonial-rule"></div>
    <p class="testimonial-text">Lorem ipsum dolor sit amet nem eos illo omnis aut aperiam ab ipsam ipsa odit aut aperiam aut aspernatur veritatis unde, sed enim accusantium laudantium sunt perspiciatis ipsam sed doloremque .....</p>
  </blockquote>
  <div class="abs arrow-btn" style="left:1008px"><svg width="14" height="18" viewBox="0 0 14 18"><path d="M11 2L4 9l7 7" fill="none" stroke="#fff" stroke-width="3"/></svg></div>
  <div class="abs arrow-btn" style="left:1059px"><svg width="14" height="18" viewBox="0 0 14 18"><path d="M3 2l7 7-7 7" fill="none" stroke="#fff" stroke-width="3"/></svg></div>
</section>

<section class="section features">
  <div class="abs feature" style="left:98px">
    <div class="feature-head"><svg width="30" height="30" viewBox="0 0 30 30"><rect x="3" y="7" width="24" height="17" rx="2" fill="none" stroke="#fff" stroke-width="3"/><rect x="3" y="11" width="24" height="4" fill="#fff"/></svg>Payment method</div>
    <div class="feature-rule"></div>
    <p class="feature-text">Lorem ipsum dolor sit amet. omnis aperiam ab ipsam ipsa odit</p>
    <div class="cards"><span></span><span></span><span></span><span></span></div>
    <div class="feature-btn">READ MORE</div>
  </div>
  <div class="abs feature mid" style="left:433px">
    <div class="feature-head"><svg width="40" height="28" viewBox="0 0 40 28"><rect x="1" y="3" width="24" height="17" fill="#fff"/><path d="M26 9h7l6 6v5H26z" fill="#fff"/><circle cx="9" cy="23" r="4" fill="#fff" stroke="#4fb3e6" stroke-width="2"/><circle cx="32" cy="23" r="4" fill="#fff" stroke="#4fb3e6" stroke-width="2"/></svg>Free shipping</div>
    <div class="feature-rule"></div>
    <p class="feature-text">Lorem ipsum dolor sit amet. omnis aperiam ab ipsam ipsa odit aut aperiam aspernatur veritatis unde enim accusantium laudantium</p>
    <div class="feature-btn">READ MORE</div>
  </div>
  <div class="abs feature" style="left:769px;width:334px">
    <div class="feature-head"><svg width="26" height="30" viewBox="0 0 26 30"><path d="M6 13V9a7 7 0 0 1 14 0v4" fill="none" stroke="#fff" stroke-width="3"/><rect x="2" y="13" width="22" height="16" rx="2" fill="#fff"/></svg>Secure shopping</div>
    <div class="feature-rule"></div>
    <p class="feature-text">Lorem ipsum dolor sit amet. omnis aperiam ab ipsam ipsa odit aut aperiam aspernatur veritatis unde enim accusantium laudantium</p>
    <div class="feature-btn">READ MORE</div>
  </div>
</section>

<footer class="section site-footer">
  <div class="abs copyright">© 2014 <b>YOUR COMPANY</b>. ALL RIGHTS RESERVED.</div>
  <nav class="abs footer-links"><span>About us</span><span>Term and use</span><span>Privacy policy</span><span>FAQs</span><span>Contact us</span></nav>
  <div class="abs social"><span></span><span></span><span></span><span></span><span></span></div>
</footer>

</body>
</html>
```